Innovative modern square business card design for law firm

We require a highly modern innovative styled SQUARE business card (double sided) design & layout for our law firm (PLUS an accompanying letterhead design), which specialises mainly in criminal defence. However included somewhere in the design should display the icons representative of all four different areas of law in which the firm offers services. Each card to display the name of the lawyer, job title, telephone number, switchboard, email, web address, facebook & twitter details + physical address. Attached is the main logo + icons of each of the other departments to be included as well as the firms main overhaul icon (all of which can be used or blended into the overall in some way.(note. high res versions of these icons can be provided if required by the design))

Law Firm

```html
<!DOCTYPE html>
<html lang="en">
<head>
<meta charset="utf-8">
<title>Harlow Defence – Business Card</title>
<link rel="stylesheet" href="https://fonts.googleapis.com/css2?family=Cinzel:wght@400;600&family=Open+Sans:wght@400;600&display=swap">
<style>
  :root {
    --navy: #123a56;
    --navy-deep: #0b2a40;
    --navy-light: #2a5a7c;
    --paper: #ffffff;
    --ink: #1c1c1c;
    --stage: #e9ebee;
    --dept-blue: #3a3f8f;
    --dept-red: #d8283a;
    --dept-green: #1f3325;
    --dept-orange: #ee7a2a;
  }
  * { box-sizing: border-box; margin: 0; padding: 0; }
  html, body { width: 1200px; height: 900px; overflow: hidden; }
  body {
    background: var(--stage);
    font-family: "Open Sans", Arial, sans-serif;
    position: relative;
  }
  .card {
    position: absolute;
    top: 190px;
    width: 520px;
    height: 520px;
    box-shadow: 0 6px 18px rgba(0,0,0,.18);
    overflow: hidden;
  }

  /* front */
  .card-front { left: 60px; background: var(--paper); }
  .card-front .base-band {
    position: absolute; left: 0; right: 0; bottom: 0; height: 48px;
    background: var(--navy);
  }
  .holder { position: absolute; right: 32px; top: 28px; text-align: right; }
  .holder-name {
    font-family: "Cinzel", Georgia, serif; font-size: 22px; color: var(--navy); letter-spacing: 1px;
  }
  .holder-title { font-size: 14px; font-weight: 600; color: var(--ink); margin-top: 2px; }
  .brand {
    position: absolute; left: 32px; top: 100px;
    display: flex; align-items: center; gap: 12px;
  }
  .brand-mark { width: 50px; height: 50px; background: var(--navy); border-radius: 6px; flex: none; }
  .brand-name {
    font-family: "Cinzel", Georgia, serif; font-weight: 600;
    font-size: 30px; line-height: 1; color: var(--navy); letter-spacing: 1px; white-space: nowrap;
  }
  .brand-hotline {
    position: absolute; left: 32px; top: 162px;
    font-size: 12px; font-weight: 600; color: var(--navy);
  }
  .address {
    position: absolute; right: 32px; top: 200px; text-align: right;
    font-size: 13px; font-weight: 600; color: var(--ink); line-height: 1.4;
  }
  .departments { position: absolute; right: 32px; top: 252px; display: flex; gap: 8px; }
  .department { width: 34px; height: 34px; border-radius: 4px; }
  .department.blue { background: var(--dept-blue); }
  .department.red { background: var(--dept-red); }
  .department.green { background: var(--dept-green); }
  .department.orange { background: var(--dept-orange); }
  .contacts { position: absolute; left: 32px; bottom: 70px; list-style: none; }
  .contacts li {
    display: flex; align-items: center; gap: 10px;
    font-size: 15px; font-weight: 600; color: var(--ink); line-height: 1.5;
  }
  .contacts svg { width: 13px; height: 13px; fill: var(--navy); flex: none; }

  /* back */
  .card-back {
    left: 620px;
    background: radial-gradient(ellipse at 62% 30%, var(--navy-light), var(--navy) 55%, var(--navy-deep));
  }
  .back-brand {
    position: absolute; left: 0; right: 0; top: 210px;
    display: flex; justify-content: center; align-items: center; gap: 16px;
  }
  .back-brand .brand-mark { width: 70px; height: 70px; background: var(--paper); border-radius: 8px; }
  .back-brand .brand-name { color: var(--paper); font-size: 36px; }
  .back-hotline {
    position: absolute; left: 0; right: 0; top: 300px; text-align: center;
    font-size: 15px; font-weight: 600; color: var(--paper);
  }
</style>
</head>
<body>
  <section class="card card-front">
    <div class="holder">
      <div class="holder-name">DORIAN VALE</div>
      <div class="holder-title">Advocate</div>
    </div>

    <div class="brand">
      <div class="brand-mark"></div>
      <div class="brand-name">Harlow Defence</div>
    </div>
    <div class="brand-hotline">0800 555 010 (24hrs)</div>

    <div class="address">P.O. Box 456, Lindon,<br>Fairview US 5678</div>
    <div class="departments">
      <div class="department blue"></div>
      <div class="department red"></div>
      <div class="department green"></div>
      <div class="department orange"></div>
    </div>

    <ul class="contacts">
      <li><svg viewBox="0 0 24 24"><path d="M6.6 10.8a15 15 0 0 0 6.6 6.6l2.2-2.2c.3-.3.7-.4 1-.2 1.1.4 2.3.6 3.6.6.6 0 1 .4 1 1V20c0 .6-.4 1-1 1A17 17 0 0 1 3 4c0-.6.4-1 1-1h3.5c.6 0 1 .4 1 1 0 1.3.2 2.5.6 3.6.1.3 0 .7-.2 1z"/></svg>0800 555 010</li>
      <li><svg viewBox="0 0 24 24"><path d="M2 5h20v14H2z M4 7v.5l8 5 8-5V7z" fill-rule="evenodd"/></svg>dvale@harlowdefence.com</li>
      <li><svg viewBox="0 0 24 24"><circle cx="12" cy="12" r="10"/></svg>www.harlowdefence</li>
      <li><svg viewBox="0 0 24 24"><circle cx="12" cy="12" r="9"/></svg>/harlowdefence</li>
      <li><svg viewBox="0 0 24 24"><circle cx="12" cy="12" r="9"/></svg>/harlowdefence</li>
    </ul>
    <div class="base-band"></div>
  </section>

  <section class="card card-back">
    <div class="back-brand">
      <div class="brand-mark"></div>
      <div class="brand-name">Harlow Defence</div>
    </div>
    <div class="back-hotline">0800 555 010 (24hrs)</div>
  </section>
</body>
</html>
```